Emergency Medical Training and Events Company Business Needs Business Card Design

We are in need of a business card for our dynamic company expanding its customer base and need to be easily contacted and identified for when we visit with government officials, potential EMS / Fire agencies and county coordinators to arrange for training programs for first responders to better prepare them for critical thinking at critical incidents.

Target Market(s)

EMS/Fire and Event Promoters

Industry/Entity Type

Medical

Contact Information for Business Card

Two cards, comparable designs:

Martin K. Halvey, Principal, m.halvey@rvqtlo.com
Owen Tash, Event and Training Specialist, o.tash@rvqtlo.com

Font styles to use
Other font styles liked:
• Cambria

Colors

Designer to choose colors to be used in the design.

Requirements
Must have
• Company Logo, Spots for Name, Title, Phone Number, Email, Website
• A bullet list stating that we offer, QRB CPR and First Aid Instructors, Hold the Line Instructors, Event EMS, CME's, MCI Training and Planning. We prefer to have a black background for the card but if you can make a blue or white card stand out we would review that as well.
Should not have
• Tacky logos or special sayings ... simple, elegant, professional is the look we seek

```html
<!DOCTYPE html>
<html lang="en">
<head>
<meta charset="utf-8">
<title>RVQ Solutions – Business Card</title>
<link rel="stylesheet" href="https://fonts.googleapis.com/css2?family=Caladea:wght@400;700&display=swap">
<style>
  :root {
    --page-bg: #ebebeb;
    --navy: #141a4a;
    --red: #c8161d;
    --red-light: #dd3a3f;
    --white: #ffffff;
    --ink: #1c1c1c;
    --card-shadow: 0 6px 12px rgba(0,0,0,0.22);
  }
  html, body {
    margin: 0;
    padding: 0;
    width: 1200px;
    height: 1200px;
    overflow: hidden;
    background: var(--page-bg);
    font-family: "Caladea", Cambria, Georgia, serif;
  }
  .card {
    position: absolute;
    left: 266px;
    width: 668px;
    height: 381px;
    box-shadow: var(--card-shadow);
    overflow: hidden;
  }
  .card--front {
    top: 146px;
    background: var(--navy);
  }
  .card--back {
    top: 643px;
    background: var(--navy);
  }

  /* Front */
  .brand {
    position: absolute;
    left: 92px;
    top: 118px;
    display: flex;
    align-items: center;
    gap: 26px;
  }
  .brand__dot {
    width: 120px;
    height: 120px;
    border-radius: 50%;
    background: var(--red);
  }
  .brand__name {
    color: var(--white);
    font-weight: 700;
    font-size: 64px;
    line-height: 1;
    letter-spacing: 1px;
  }
  .website {
    position: absolute;
    left: 0;
    right: 0;
    top: 332px;
    text-align: center;
    color: var(--white);
    font-size: 19px;
  }

  /* Back */
  .back-art {
    position: absolute;
    inset: 0;
    width: 668px;
    height: 381px;
  }
  .offer {
    position: absolute;
    left: 22px;
    top: 24px;
    color: var(--white);
  }
  .offer__title {
    margin: 0 0 14px;
    color: var(--red);
    font-weight: 700;
    font-size: 21px;
    letter-spacing: 0.5px;
  }
  .offer__list {
    list-style: none;
    margin: 0;
    padding: 0;
  }
  .offer__item {
    position: relative;
    padding-left: 18px;
    font-size: 19px;
    line-height: 34.4px;
  }
  .offer__item::before {
    content: "\2731";
    position: absolute;
    left: 0;
    top: 0;
    font-size: 12px;
  }
  .contact {
    position: absolute;
    right: 28px;
    top: 198px;
    text-align: right;
  }
  .contact__name {
    margin: 0;
    color: var(--red);
    font-weight: 700;
    font-size: 29px;
    line-height: 1.2;
  }
  .contact__title {
    margin: 0;
    color: var(--ink);
    font-size: 20px;
    line-height: 29px;
  }
  .contact__details {
    margin-top: 10px;
    color: var(--red);
    font-weight: 700;
    font-size: 22px;
    line-height: 29px;
  }
</style>
</head>
<body>

<section class="card card--front">
  <div class="brand">
    <span class="brand__dot"></span>
    <span class="brand__name">RVQ Solutions</span>
  </div>
  <div class="website">www.rvqtlo.com</div>
</section>

<section class="card card--back">
  <svg class="back-art" viewBox="0 0 668 381" aria-hidden="true">
    <path d="M592 0 L668 0 L668 381 L350 381 C352 230 470 110 592 0 Z" fill="var(--white)"/>
    <path d="M556 0 L592 0 C470 110 352 230 350 381 L338 381 C338 225 440 110 556 0 Z" fill="var(--red)"/>
    <path d="M575 0 L592 0 C470 110 352 230 350 381 L345 381 C348 230 458 112 575 0 Z" fill="var(--red-light)" opacity="0.6"/>
  </svg>

  <div class="offer">
    <h2 class="offer__title">WE OFFER</h2>
    <ul class="offer__list">
      <li class="offer__item">QRB CPR &amp; First Aid Instructors</li>
      <li class="offer__item">Hold the Line Instructors</li>
      <li class="offer__item">Event EMS</li>
      <li class="offer__item">CME's</li>
      <li class="offer__item">MCI Training and Planning</li>
    </ul>
  </div>

  <div class="contact">
    <p class="contact__name">Owen Tash</p>
    <p class="contact__title">Event &amp; Training<br>Specialist</p>
    <div class="contact__details">
      <div class="contact__email">o.tash@rvqtlo.com</div>
      <div class="contact__phone">000000 000000</div>
    </div>
  </div>
</section>

</body>
</html>
```